Printing company needs stellar web site!

We need a website for a printing company based in Atlanta, Georgia, USA. Our company is 26 years old and just this year did a logo and branding refresh. Now we need our website to be refreshed as well.

Please see the attached source files for our new logo and stationary design.

Printing

```html
<!DOCTYPE html>
<html lang="en">
<head>
<meta charset="utf-8">
<title>Inkwell – Digital Printing</title>
<link rel="stylesheet" href="https://fonts.googleapis.com/css2?family=Jura:wght@500;600&family=Open+Sans:wght@700&family=Arimo:wght@400;700&family=Quicksand:wght@400&display=swap">
<style>
:root{
  --blue:#0a78c8;
  --blue-dark:#0d4f86;
  --pink:#e0107e;
  --ink:#2b2b2b;
  --text:#444;
  --grey-bg:#e9e9e9;
  --line:#d4d4d4;
  --white:#fff;
}
*{margin:0;padding:0;box-sizing:border-box}
html,body{width:1034px;height:1200px;overflow:hidden;background:var(--white)}
body{position:relative;font-family:"Arimo",Arial,sans-serif;color:var(--text)}
.abs{position:absolute}

.site-header{left:0;top:0;width:1034px;height:97px;background:linear-gradient(90deg,#f2f2f2,#e6e6e6 60%,#f0f0f0)}
.brand{left:97px;top:30px;display:flex;align-items:center;gap:10px;font-family:"Jura",sans-serif;font-weight:600;font-size:38px;color:var(--blue);letter-spacing:1px}
.brand-dot{width:30px;height:30px;border-radius:50%;background:var(--blue)}
.call-line{right:86px;top:18px;font-family:"Jura",sans-serif;font-weight:600;font-size:16px;color:var(--pink);letter-spacing:.5px}
.phone{right:88px;top:44px;display:flex;align-items:center;gap:12px;font-size:31px;color:var(--ink)}

.main-nav{left:0;top:97px;width:1034px;height:50px;background:var(--blue)}
.main-nav a{position:absolute;top:17px;font-family:"Open Sans",sans-serif;font-weight:700;font-size:13px;color:var(--white);text-decoration:none;letter-spacing:.2px}

.hero{left:0;top:147px;width:1034px;height:302px;background:radial-gradient(circle at 50% 40%,#fafafa,#dcdcdc)}
.hero-title{font-family:"Quicksand",sans-serif;font-weight:400;font-size:62px;line-height:1}
.hero-title.top{left:176px;top:20px;color:var(--blue)}
.hero-title.bottom{left:84px;top:66px;color:var(--pink)}
.paper-stack{left:86px;top:181px;width:376px;height:121px;background:linear-gradient(90deg,#c79ae6,#f2a6c8 50%,#f1e08a)}
.printer-photo{left:569px;top:21px;width:366px;height:259px;background:linear-gradient(135deg,#cfcfcf,#4a78c8 50%,#bdbdbd)}

.welcome{left:0;top:449px;width:1034px;height:271px;background:var(--white);text-align:center}
.welcome h1{position:absolute;left:0;width:1034px;top:34px;font-family:"Jura",sans-serif;font-weight:500;font-size:40px;color:var(--ink);letter-spacing:1px}
.welcome h1 span{color:var(--blue)}
.welcome p{position:absolute;left:89px;width:820px;top:97px;font-size:12.5px;line-height:19px;color:var(--text)}
.btn-more{left:404px;top:198px;width:219px;height:38px;border-radius:10px;background:linear-gradient(#1a8ad6,#07569c);color:var(--white);font-family:"Jura",sans-serif;font-weight:600;font-size:21px;line-height:38px;letter-spacing:1px;box-shadow:0 6px 6px -4px rgba(0,0,0,.35)}

.showcase{left:0;top:720px;width:1034px;height:409px;background:var(--grey-bg)}
.panel{position:absolute;background:var(--white);border:1px solid var(--line);border-radius:3px}
.panel-head{height:34px;color:var(--white);font-family:"Jura",sans-serif;font-weight:600;font-size:24px;line-height:34px;padding-left:24px;border-radius:3px 3px 0 0}
.featured{left:88px;top:32px;width:568px;height:326px}
.featured .panel-head{background:var(--blue)}
.product{position:absolute;top:46px;width:154px}
.product-thumb{height:192px;border:1px solid var(--line);padding:8px}
.product-thumb div{width:100%;height:100%}
.product-name{margin:10px 0 0 4px;font-family:"Open Sans",sans-serif;font-weight:700;font-size:12.5px;color:var(--pink);letter-spacing:.4px}
.product-desc{margin:4px 0 0 4px;font-size:10.5px;color:var(--ink)}
.product-buy{display:flex;align-items:center;justify-content:space-between;margin:9px 10px 0 6px;font-family:"Open Sans",sans-serif;font-weight:700;font-size:12px;color:var(--pink)}
.add-cart{background:var(--blue);color:var(--white);font-family:"Arimo",sans-serif;font-weight:400;font-size:11px;padding:4px 6px}

.categories{left:684px;top:32px;width:264px;height:323px}
.categories .panel-head{background:var(--pink)}
.cat-list{list-style:none;margin-top:12px}
.cat-list li{position:relative;height:36px;line-height:30px;padding-left:30px;font-size:15.5px;color:var(--ink)}
.cat-list li.active{background:#f1f1f1;height:30px;margin-bottom:6px}
.cat-list li.active svg{position:absolute;right:12px;top:9px}

.site-footer{left:0;top:1129px;width:1034px;height:71px;background:var(--blue-dark);color:var(--white)}
.footer-links{left:95px;top:16px;font-size:12px}
.footer-links span{margin:0 9px}
.copyright{left:95px;top:40px;font-size:12px}
.footer-brand{right:86px;top:16px;display:flex;align-items:center;gap:8px;font-family:"Jura",sans-serif;font-weight:600;font-size:28px;color:#dce6ef;letter-spacing:1px}
.footer-brand .brand-dot{width:22px;height:22px;background:#dce6ef}
</style>
</head>
<body>

<header class="site-header abs">
  <div class="brand abs"><span class="brand-dot"></span>INKWELL</div>
  <div class="call-line abs">For Appointment Call Us Today</div>
  <div class="phone abs">
    <svg width="24" height="38" viewBox="0 0 24 38" aria-hidden="true">
      <rect x="1" y="4" width="22" height="33" rx="2" fill="#1d1d1d"/>
      <rect x="14" y="0" width="4" height="6" fill="#1d1d1d"/>
      <rect x="5" y="9" width="14" height="8" fill="#fff"/>
      <g fill="#fff"><rect x="5" y="21" width="3" height="3"/><rect x="10.5" y="21" width="3" height="3"/><rect x="16" y="21" width="3" height="3"/><rect x="5" y="26" width="3" height="3"/><rect x="10.5" y="26" width="3" height="3"/><rect x="16" y="26" width="3" height="3"/><rect x="5" y="31" width="3" height="3"/><rect x="10.5" y="31" width="3" height="3"/><rect x="16" y="31" width="3" height="3"/></g>
    </svg>
    404 555 0182
  </div>
</header>

<nav class="main-nav abs">
  <a href="#" style="left:87px">CORPORATE IDENTITY</a>
  <a href="#" style="left:291px">NOTEPAD</a>
  <a href="#" style="left:421px">POSTER</a>
  <a href="#" style="left:533px">PRESENTATION FOLDER</a>
  <a href="#" style="left:746px">PROMOTIONAL PRODUCTS</a>
</nav>

<section class="hero abs">
  <div class="hero-title top abs">Digtal</div>
  <div class="hero-title bottom abs">Printing</div>
  <div class="paper-stack abs" role="img" aria-label="Photo of fanned coloured paper sheets"></div>
  <div class="printer-photo abs" role="img" aria-label="Photo of two large-format printers producing posters"></div>
</section>

<section class="welcome abs">
  <h1>Welcome to <span>Ink</span>well</h1>
  <p>simply dummy text of the printing and typesetting industry. Lorem Ipsum has been the industry's standard dummy text ever since the 1500s, when an unknown printer took a galley of type and scrambled it to make a type specimen book. It has survived not only five centuries, but also the leap into electronic typesetting, remaining essentially unchanged. It was popularised a type specimen book. It has survived not only five centuries, but also the leap into electronic typesetting, remaining essentiallyin the 1960s with the release of Letraset sheets containing</p>
  <div class="btn-more abs">More Information</div>
</section>

<section class="showcase abs">
  <div class="panel featured">
    <div class="panel-head">Featured Product</div>
    <div class="product" style="left:17px">
      <div class="product-thumb"><div role="img" aria-label="Design magazine cover" style="background:linear-gradient(160deg,#f3f3f3,#f7b6c8 40%,#f2d024 65%,#e5402f)"></div></div>
      <div class="product-name">Lorem Ipsum</div>
      <div class="product-desc">Lorem Ipsum has been the</div>
      <div class="product-buy">$ 123.00<span class="add-cart">Add to Cart</span></div>
    </div>
    <div class="product" style="left:207px">
      <div class="product-thumb"><div role="img" aria-label="Creative magazine cover" style="background:linear-gradient(160deg,#2c3a4a,#5b8fb0 40%,#d4663c 70%,#f2c24b)"></div></div>
      <div class="product-name">Lorem Ipsum</div>
      <div class="product-desc">Lorem Ipsum has been the</div>
      <div class="product-buy">$ 123.00<span class="add-cart">Add to Cart</span></div>
    </div>
    <div class="product" style="left:392px">
      <div class="product-thumb"><div role="img" aria-label="Row of coloured presentation folders" style="background:linear-gradient(90deg,#fff 8%,#1a1a1a 14%,#d8232a 32%,#f2b81c 50%,#1b9b8a 66%,#1e64b8 82%,#fff 92%)"></div></div>
      <div class="product-name">Lorem Ipsum</div>
      <div class="product-desc">Lorem Ipsum has been the</div>
      <div class="product-buy">$ 123.00<span class="add-cart">Add to Cart</span></div>
    </div>
  </div>

  <div class="panel categories">
    <div class="panel-head">Caregories</div>
    <ul class="cat-list">
      <li class="active">Presentation
        <svg width="14" height="12" viewBox="0 0 14 12" aria-hidden="true"><path d="M1 1l5 5-5 5M7 1l5 5-5 5" fill="none" stroke="#333" stroke-width="2"/></svg>
      </li>
      <li>Letterheads &amp; Envelopes</li>
      <li>Stickers</li>
      <li>Products</li>
      <li>Quality</li>
      <li>Letterhead</li>
      <li>Stickers</li>
    </ul>
  </div>
</section>

<footer class="site-footer abs">
  <div class="footer-links abs">Corporate Identity<span>|</span>Notepad<span>|</span>Poster<span>|</span>Presentation Folder<span>|</span>Promotional Products</div>
  <div class="copyright abs">© 2014 INKWELL. All Rights Reserved.</div>
  <div class="footer-brand abs"><span class="brand-dot"></span>INKWELL</div>
</footer>

</body>
</html>
```